Sales Tip from Ned Valcourt- Think Like a Buyer-

I am a sales trainer for B2B sales teams. I would like you to create an infographic that my learners can view, easily understand and immediately apply to their day to day work.
The graphic should:
1-Display the title on top- Sales Tip from Ned Valcourt- Think Like a Buyer
2- Please use the writing and layout from the attachment.
3- Create a tagline at the bottom that says- Top B2B Sales Teams, Sell The Way Thier Clients Buy.
Our company colors are red, silver with slight black trim.
I do not like cartoon like graphics. This must be poweful...
Updates

thank you very much for your consideration. looking forward to seeing your work Ned

Target Market(s)

CEO's of B2B Technology Companies

Font styles to use
Sans Serif

Requirements
Must have
• the apility to attach to a powerpoint slide. company colors...red, silver and a little black
Should not have
• cartoon animation, business,

```html
<!DOCTYPE html>
<html lang="en">
<head>
<meta charset="UTF-8">
<title>Sales Tip from Ned Valcourt: Think Like a Buyer</title>
<link rel="stylesheet" href="https://fonts.googleapis.com/css2?family=Montserrat:wght@400;500&family=Playfair+Display:wght@700&family=Cabin:wght@400&display=swap">
<style>
  :root {
    --header-black: #222222;
    --silver: #b3b3b3;
    --silver-dark: #9a9a9a;
    --panel-red: #9b0f00;
    --panel-red-deep: #760a00;
    --panel-red-shadow: #4f0600;
    --rule-black: #1a0000;
    --text-white: #ffffff;
    --tagline: #f2f2f2;
  }
  html, body {
    margin: 0;
    padding: 0;
    width: 1200px;
    height: 900px;
    overflow: hidden;
  }
  .slide {
    position: relative;
    width: 1200px;
    height: 900px;
    background: var(--silver);
    overflow: hidden;
  }
  .side-curve {
    position: absolute;
    left: 0;
    top: 0;
  }
  .slide-header {
    position: absolute;
    left: 0;
    top: 0;
    width: 1200px;
    height: 108px;
    background: var(--header-black);
  }
  .slide-title {
    position: absolute;
    left: 32px;
    right: 32px;
    top: 36px;
    margin: 0;
    font-family: "Montserrat", sans-serif;
    font-weight: 500;
    font-size: 28px;
    line-height: 1;
    letter-spacing: 0.19em;
    color: var(--text-white);
    white-space: nowrap;
  }
  .panel {
    position: absolute;
    top: 150px;
    height: 602px;
    background: var(--panel-red);
  }
  .panel--seller { left: 70px; width: 488px; }
  .panel--buyer { left: 638px; width: 491px; }
  .panel::before {
    content: "";
    position: absolute;
    left: 0;
    right: 0;
    top: 580px;
    height: 3px;
    background: var(--panel-red-deep);
  }
  .panel::after {
    content: "";
    position: absolute;
    left: 0;
    right: 0;
    bottom: 0;
    height: 11px;
    background: var(--panel-red-shadow);
  }
  .panel-heading {
    position: absolute;
    left: 0;
    right: 0;
    top: 40px;
    margin: 0;
    text-align: center;
    font-family: "Playfair Display", serif;
    font-weight: 700;
    font-size: 32px;
    line-height: 40px;
    letter-spacing: 0.14em;
    color: var(--text-white);
  }
  .panel-rule {
    position: absolute;
    top: 87px;
    left: 84px;
    width: 320px;
    height: 3px;
    background: var(--rule-black);
  }
  .panel--buyer .panel-rule { left: 92px; }
  .question {
    position: absolute;
    left: 0;
    right: 0;
    margin: 0;
    text-align: center;
    font-family: "Cabin", sans-serif;
    font-size: 25px;
    line-height: 35px;
    color: var(--text-white);
  }
  .footer-rule {
    position: absolute;
    left: 66px;
    top: 801px;
    width: 1068px;
    height: 3px;
    background: #111111;
  }
  .tagline {
    position: absolute;
    left: 70px;
    top: 832px;
    margin: 0;
    font-family: "Montserrat", sans-serif;
    font-weight: 400;
    font-size: 26px;
    line-height: 1;
    letter-spacing: 0.225em;
    color: var(--tagline);
    white-space: nowrap;
  }
</style>
</head>
<body>
<main class="slide">
  <svg class="side-curve" width="1200" height="900" viewBox="0 0 1200 900" aria-hidden="true">
    <path d="M1148 108 Q1212 480 1112 900 L1200 900 L1200 108 Z" fill="var(--silver-dark)"/>
  </svg>

  <header class="slide-header">
    <h1 class="slide-title">SALES TIP FROM NED VALCOURT: THINK LIKE A BUYER</h1>
  </header>

  <section class="panel panel--seller">
    <h2 class="panel-heading">SELLER</h2>
    <div class="panel-rule"></div>
    <p class="question" style="top:128px;">- Do they like us?</p>
    <p class="question" style="top:186px;">- Do they like our product better<br>than the competition?</p>
    <p class="question" style="top:284px;">- Will they accept our price?</p>
    <p class="question" style="top:357px;">- Can we close it quickly<br>without being to pushy?</p>
  </section>

  <section class="panel panel--buyer">
    <h2 class="panel-heading">BUYER</h2>
    <div class="panel-rule"></div>
    <p class="question" style="top:128px;">- How will this impact our business?</p>
    <p class="question" style="top:186px;">- What risks or disruptions<br>could occur?</p>
    <p class="question" style="top:282px;">- Why do we need to do this now?</p>
    <p class="question" style="top:358px;">- Why them and not the competition?</p>
    <p class="question" style="top:426px;">- What are all the costs?<br>Is it a fair deal?</p>
  </section>

  <div class="footer-rule"></div>
  <p class="tagline">TOP B2B SALES TEAMS SELL THE WAY THIER CLIENTS BUY</p>
</main>
</body>
</html>
```